Moravel Stenwick Inc needs a business card design

Looking for a unique, classy and sharp business card design.

Contact Information for Business Card

Moravel Stenwick Inc.
Marisa Ortega Bellido BScOT(c)
Occupational Therapist
(780) 555-0142
moravelstenwick@postlynx.net

```html
<!DOCTYPE html>
<html lang="en">
<head>
<meta charset="utf-8">
<title>Moravel Stenwick Inc. — Business Card</title>
<link rel="stylesheet" href="https://fonts.googleapis.com/css2?family=Roboto:wght@400;500;700&display=swap">
<style>
  :root {
    --bg: #e9e7e6;
    --card-white: #ffffff;
    --purple: #9c3aa2;
    --green: #86c440;
    --ink: #3a3a3a;
    --shadow: rgba(0, 0, 0, 0.18);
  }
  * { margin: 0; padding: 0; box-sizing: border-box; }
  html, body {
    width: 1200px;
    height: 764px;
    overflow: hidden;
    background: var(--bg);
    font-family: "Roboto", Arial, sans-serif;
  }
  .canvas {
    position: relative;
    width: 1200px;
    height: 764px;
  }
  .card {
    position: absolute;
    top: 239px;
    width: 500px;
    height: 286px;
    box-shadow: 0 6px 18px var(--shadow);
    overflow: hidden;
  }
  /* Front */
  .card-front {
    left: 60px;
    background: var(--card-white);
  }
  .holder {
    position: absolute;
    top: 34px;
    right: 34px;
    text-align: right;
  }
  .holder-name {
    color: var(--purple);
    font-size: 17px;
    font-weight: 400;
    letter-spacing: 0.2px;
  }
  .holder-title {
    color: var(--green);
    font-size: 14px;
    font-weight: 400;
    margin-top: 2px;
  }
  .brand {
    position: absolute;
    display: flex;
    align-items: center;
    gap: 10px;
  }
  .brand-dot {
    width: 16px;
    height: 16px;
    border-radius: 50%;
    background: var(--green);
    flex: none;
  }
  .brand-name {
    color: var(--purple);
    font-weight: 700;
    white-space: nowrap;
  }
  .card-front .brand {
    left: 36px;
    bottom: 80px;
  }
  .card-front .brand-name { font-size: 24px; }
  .contact {
    position: absolute;
    right: 34px;
    bottom: 52px;
    list-style: none;
    text-align: right;
  }
  .contact-item {
    display: flex;
    align-items: center;
    justify-content: flex-end;
    gap: 10px;
    color: var(--ink);
    font-size: 15px;
    line-height: 24px;
  }
  .contact-icon {
    width: 14px;
    height: 14px;
    fill: var(--purple);
    flex: none;
  }
  /* Back */
  .card-back {
    left: 640px;
    background: linear-gradient(90deg, var(--purple) 0 48%, var(--green) 48% 100%);
  }
  .back-panel {
    position: absolute;
    left: 50%;
    top: 50%;
    width: 290px;
    height: 180px;
    transform: translate(-50%, -50%);
    background: var(--card-white);
    border-radius: 14px;
    display: flex;
    align-items: center;
    justify-content: center;
  }
  .back-panel .brand { position: static; }
  .back-panel .brand-name { font-size: 22px; }
</style>
</head>
<body>
  <main class="canvas">
    <section class="card card-front" aria-label="Business card front">
      <div class="holder">
        <p class="holder-name">Marisa Ortega Bellido BScOT(c)</p>
        <p class="holder-title">Occupational Therapist</p>
      </div>
      <div class="brand">
        <span class="brand-dot"></span>
        <span class="brand-name">Moravel Stenwick Inc.</span>
      </div>
      <ul class="contact">
        <li class="contact-item">
          <span>(780) 555-0142</span>
          <svg class="contact-icon" viewBox="0 0 24 24" aria-hidden="true"><path d="M6.6 10.8a15.1 15.1 0 0 0 6.6 6.6l2.2-2.2a1 1 0 0 1 1-.25 11.4 11.4 0 0 0 3.6.57 1 1 0 0 1 1 1V20a1 1 0 0 1-1 1A17 17 0 0 1 3 4a1 1 0 0 1 1-1h3.5a1 1 0 0 1 1 1c0 1.25.2 2.45.57 3.57a1 1 0 0 1-.25 1z"/></svg>
        </li>
        <li class="contact-item">
          <span>moravelstenwick@postlynx.net</span>
          <svg class="contact-icon" viewBox="0 0 24 24" aria-hidden="true"><path d="M2 5h20v14H2z M3.5 6.5 12 13l8.5-6.5" fill="var(--purple)" stroke="#fff" stroke-width="1.4"/></svg>
        </li>
      </ul>
    </section>

    <section class="card card-back" aria-label="Business card back">
      <div class="back-panel">
        <div class="brand">
          <span class="brand-dot"></span>
          <span class="brand-name">Moravel Stenwick Inc.</span>
        </div>
      </div>
    </section>
  </main>
</body>
</html>
```